Visitenkarten-Design für aufstrebendes, modernes und innovatives Elektrounternehmen
Zielgruppe
Unsere Firma ist im Bereich Elektro- und Gebäudetechnik angesiedelt.
Zielgruppe sind Privatkunden und Geschäftskunden.
Wir machen alles rund um das Thema Elektrotechnik, Elektroinstallation ....
Aufgabenstellung
Es soll ein ansprechendes modernes Design sein. Gerne auch mit Rückseite.
Wir sind ein junges aufstrebendes modernes und innovatives Unternehmen

```html
<!DOCTYPE html>
<html lang="de">
<head>
<meta charset="utf-8">
<title>Feldmar – Visitenkarte</title>
<link href="https://fonts.googleapis.com/css2?family=Open+Sans:wght@400;600;800&display=swap" rel="stylesheet">
<style>
  :root {
    --bg: #e9e7e3;
    --card-dark: #58595b;
    --card-light: #ffffff;
    --ink: #1f1f1f;
    --ink-soft: #4d4e50;
    --teal: #5a9fb0;
    --olive: #b5b12e;
    --ring: rgba(255,255,255,0.05);
  }
  * { box-sizing: border-box; margin: 0; padding: 0; }
  html, body { width: 1200px; height: 822px; overflow: hidden; }
  body {
    background: var(--bg);
    font-family: "Open Sans", Arial, sans-serif;
    display: flex; align-items: center; justify-content: center; gap: 40px;
  }
  .card {
    position: relative; width: 560px; height: 362px; overflow: hidden;
    box-shadow: 0 10px 28px rgba(0,0,0,0.22);
  }

  /* Rückseite */
  .card--back { background: var(--card-dark); color: #fff; }
  .back__ring {
    position: absolute; left: 130px; top: -70px; width: 380px; height: 380px;
    border-radius: 50%; border: 46px solid var(--ring);
  }
  .brand { position: absolute; display: flex; align-items: center; gap: 12px; }
  .brand__dot { width: 70px; height: 70px; border-radius: 50%; background: var(--olive); flex: none; }
  .brand__text { display: flex; flex-direction: column; line-height: 1; }
  .brand__name { font-weight: 800; font-size: 54px; letter-spacing: -1px; }
  .brand__sub { font-weight: 600; font-size: 11.5px; color: var(--teal); text-transform: uppercase; letter-spacing: 0.6px; margin-top: 4px; padding-left: 40px; }
  .card--back .brand { left: 120px; top: 110px; }
  .card--back .brand__name { color: #fff; }
  .back__tagline {
    position: absolute; left: 0; right: 0; top: 255px; text-align: center;
    text-transform: uppercase; font-size: 13px; letter-spacing: 1.4px; line-height: 1.6;
  }

  /* Vorderseite */
  .card--front { background: var(--card-light); color: var(--ink); }
  .card--front .brand { right: 34px; top: 28px; }
  .card--front .brand__dot { width: 62px; height: 62px; }
  .card--front .brand__name { color: var(--ink-soft); font-size: 46px; }
  .card--front .brand__sub { font-size: 10px; padding-left: 34px; }
  .rule { position: absolute; height: 1px; background: var(--teal); }
  .rule--top { left: 230px; right: 34px; top: 112px; }
  .rule--mid { left: 34px; width: 220px; top: 190px; }
  .person { position: absolute; left: 34px; top: 130px; }
  .person__name { color: var(--teal); font-weight: 600; font-size: 24px; line-height: 1.1; }
  .person__role { font-size: 14px; margin-top: 3px; }
  .address { position: absolute; right: 34px; top: 140px; text-align: right; font-size: 14px; line-height: 1.45; }
  .contacts { position: absolute; left: 34px; top: 206px; list-style: none; font-size: 15px; line-height: 1.55; }
  .contacts li { display: flex; align-items: center; gap: 12px; }
  .contacts svg { width: 15px; height: 15px; fill: var(--teal); flex: none; }
  .swoosh { position: absolute; left: 0; bottom: 0; width: 560px; height: 362px; }
  .website { position: absolute; right: 22px; bottom: 22px; color: #fff; font-size: 14px; }
</style>
</head>
<body>

  <section class="card card--back" aria-label="Rückseite">
    <div class="back__ring"></div>
    <div class="brand">
      <span class="brand__dot"></span>
      <span class="brand__text">
        <span class="brand__name">Feldmar</span>
        <span class="brand__sub">Elektro- &amp; Gebäudetechnik</span>
      </span>
    </div>
    <p class="back__tagline">Ihr Innungsmeisterbetrieb<br>für innovative Elektro-und Gebäudetechnik</p>
  </section>

  <section class="card card--front" aria-label="Vorderseite">
    <div class="brand">
      <span class="brand__dot"></span>
      <span class="brand__text">
        <span class="brand__name">Feldmar</span>
        <span class="brand__sub">Elektro- &amp; Gebäudetechnik</span>
      </span>
    </div>
    <div class="rule rule--top"></div>

    <div class="person">
      <p class="person__name">Jonas Feldmar</p>
      <p class="person__role">Elektrotechnikermeister</p>
    </div>
    <div class="rule rule--mid"></div>

    <p class="address">Lindenweg 7<br>79312 Halmbach</p>

    <ul class="contacts">
      <li><svg viewBox="0 0 16 16"><path d="M3 1l3 3-1.5 2a8 8 0 0 0 5.5 5.5L12 10l3 3-2 2C6 15 1 10 1 3z"/></svg>04711 386214</li>
      <li><svg viewBox="0 0 16 16"><path d="M4 1h8v4H4zM1 6h14v6h-3v3H4v-3H1zM5 10v4h6v-4z"/></svg>04711 386200</li>
      <li><svg viewBox="0 0 16 16"><path d="M1 3h14v10H1zM2 4l6 5 6-5v1L8 10 2 5z" fill-rule="evenodd"/></svg>info@feldmar-licht-elektro.de</li>
    </ul>

    <svg class="swoosh" viewBox="0 0 560 362" aria-hidden="true">
      <path d="M0 362 L0 346 C200 338 400 318 560 282 L560 362 Z" fill="var(--teal)"/>
      <path d="M0 336 C170 330 340 306 470 272 C350 312 180 334 0 342 Z" fill="var(--olive)"/>
    </svg>
    <p class="website">www.feldmar-elektrotechnik.de</p>
  </section>

</body>
</html>
```